Healthcare/Medical Consultant Company

KRT is a Healthcare Conultant Company. We help doctors manage the business side of their medical practice.
We already have a very basic world press design. We want an upgraded design that conveys partnership, healthcare expertise and healthcare innovation to our client. It needs to have a sleek, clean, modern and inclusive look. Pictures need need to convey diversity (including pictures of people of all races and shows both men and women working together in a healthcare environment to make it better). The Pictures on the home page should particularly illustrate diversity and Healthcare expertise. The company logo is blue and white but the site doesn’t have to follow the exact same theme but the logo needs to blend well with the chosen theme. The logo should ideally be in the header of the website. We would also like the following included in our website:

1. Pages should include: a home page, About Us page, Services page, Get a quote page, Contact Us page, Staff page(where we can add pictures and bio for staff).

2. The Drop down menu for services should have hyperlinks ( for each service)Leading to a page that provides detailed info about that specific service. Our services include: Revenue Cycle Management, Regulatory Compliance, Human Resources Management, & practice Management.

3. Links to social media should in the header or footer of each page.

4. Contact info should be in the footer of each page.

5. Clients should be an email to us from the contact page.

Target Market(s)

Physician Medical Practices

Industry/Entity Type

Medical

Coding

Coded - Design and coding required

Font styles to use
Sans Serif

Colors

Designer to choose colors to be used in the design.

Requirements
Must have
• See project description
Nice to have
• See project description

```html
<!DOCTYPE html>
<html lang="en">
<head>
<meta charset="utf-8">
<title>KRT – Keystone Health Partners</title>
<link href="https://fonts.googleapis.com/css2?family=Montserrat:wght@400;500;600;700;800&family=Open+Sans:wght@400;600&display=swap" rel="stylesheet">
<style>
:root{
  --blue:#2b8fd3;
  --blue-light:#4aa3dd;
  --navy:#173f8e;
  --navy-dark:#12306e;
  --ink:#1d1d1f;
  --text:#444;
  --grey-bg:#eef0f3;
  --footer:#232426;
  --white:#fff;
}
*{box-sizing:border-box;margin:0;padding:0}
html,body{width:1200px;height:4054px;overflow:hidden}
body{position:relative;font-family:"Open Sans",sans-serif;color:var(--text);background:var(--white)}
.abs{position:absolute}
h1,h2,h3,h4,.nav,.btn{font-family:"Montserrat",sans-serif}
.btn{position:absolute;display:flex;align-items:center;justify-content:center;color:#fff;font-weight:700;text-decoration:none}

/* header */
.site-header{position:absolute;left:0;top:0;width:1200px;height:135px;background:#fff}
.brand{left:130px;top:22px;width:300px;text-align:center}
.brand-mark{font-family:"Montserrat",sans-serif;font-size:54px;font-weight:800;color:var(--navy);letter-spacing:2px;line-height:60px}
.brand-name{font-family:"Montserrat",sans-serif;font-size:15px;font-weight:500;color:var(--navy);margin-top:4px}
.call{left:872px;top:22px;display:flex;gap:10px;align-items:center}
.call small{display:block;font:700 11px "Montserrat",sans-serif;color:var(--ink)}
.call strong{font:700 20px "Montserrat",sans-serif;color:var(--navy)}
.nav{left:555px;top:88px;display:flex;gap:0;font-size:12.5px;font-weight:700;color:var(--ink)}
.nav span{padding:8px 14px}
.nav .active{background:var(--blue);color:#fff}

/* hero */
.hero{left:0;top:135px;width:1200px;height:590px}
.hero-title{left:790px;top:298px;font:400 44px/48px "Montserrat",sans-serif;color:var(--navy)}
.hero-title b{font-weight:800;font-size:48px}
.dots{left:530px;top:650px;display:flex;gap:12px}
.dots i{width:11px;height:11px;border-radius:50%;background:#fff;display:block}
.dots i.on{background:transparent;border:2px solid #fff;width:14px;height:14px;margin-top:-1px}

/* welcome */
.welcome{left:0;top:700px;width:1200px;height:600px;background:var(--blue)}
.welcome-photo{left:152px;top:775px;width:368px;height:450px;border:6px solid #fff;background:linear-gradient(160deg,#c9d3dc,#7f8c99 60%,#e6e9ee)}
.welcome-kicker{left:598px;top:803px;font:400 30px "Montserrat",sans-serif;color:#fff}
.welcome-title{left:598px;top:848px;font:700 36px "Montserrat",sans-serif;color:#fff}
.welcome-copy{left:598px;top:925px;width:500px;font-size:14.5px;line-height:21px;color:#e9f3fb}

/* services */
.services{left:0;top:1300px;width:1200px;height:755px;background:var(--grey-bg)}
.section-title{position:absolute;width:1200px;text-align:center;font:700 36px "Montserrat",sans-serif}
.rule{position:absolute;left:570px;width:60px;height:4px;background:#c7cbd1}
.card{position:absolute;top:1515px;width:280px;height:350px;background:#fff;box-shadow:0 4px 14px rgba(0,0,0,.08);text-align:center;padding:0 20px}
.card svg{margin-top:32px}
.card h3{font-size:15px;font-weight:800;color:var(--ink);margin-top:18px;line-height:19px}
.card p{font-size:13.5px;line-height:20px;margin-top:20px;color:#444}

/* contact */
.contact-title{left:85px;top:2160px;font:700 32px "Montserrat",sans-serif;color:var(--ink)}
.contact-item{left:88px;display:flex;gap:14px;font-size:15px;color:var(--ink);line-height:21px}
.field{position:absolute;border:1px solid #bfc3c8;background:#fff;font-size:11px;color:#555;padding:8px 10px}
.contact-photo{left:515px;top:2150px;width:595px;height:500px;background:linear-gradient(170deg,#e5e9ee,#5e7ea8 45%,#24446f)}
.caption{left:560px;top:2565px;width:510px;height:135px;background:#fff;box-shadow:0 6px 20px rgba(0,0,0,.15);border-top:6px solid var(--blue)}
.caption h4{position:absolute;left:52px;top:30px;font:700 27px/34px "Montserrat",sans-serif;color:var(--navy-dark)}
.caption h4 span{color:var(--blue)}

/* newsletter */
.newsletter{left:0;top:2825px;width:1200px;height:430px;background:linear-gradient(#2154a2,#1b4690)}
.news-card{position:absolute;top:3080px;width:255px;height:335px;background:#fff;box-shadow:0 5px 16px rgba(0,0,0,.18)}
.news-card .ph{height:175px;background:linear-gradient(160deg,#dfe6ee,#4f78a8 55%,#c7d3df)}
.news-card .body{position:absolute;left:14px;top:150px;width:230px;height:165px;background:#fff;border-left:4px solid var(--blue);padding:14px 12px}
.news-card h4{font-size:13px;font-weight:700;color:var(--ink);line-height:16px}
.news-card p{font-size:10.5px;line-height:14px;margin-top:12px;color:#555}
.news-card .more{position:absolute;right:10px;bottom:10px;background:var(--navy);color:#fff;font:700 10.5px "Montserrat",sans-serif;padding:5px 10px}
.arrow{position:absolute;top:3238px;width:34px;height:34px;border-radius:50%;background:var(--blue-light);display:flex;align-items:center;justify-content:center}

/* footer */
.site-footer{left:0;top:3667px;width:1200px;height:387px;background:var(--footer);color:#d6d6d6}
.footer-brand{left:140px;top:3760px;width:280px;text-align:center}
.footer-brand .brand-mark{color:#2f5fb0}
.footer-brand .brand-name{color:#9fb2d6}
.foot-col h4{font-size:12px;font-weight:700;color:#fff;margin-bottom:16px}
.foot-col{position:absolute;top:3735px;font-size:11.5px;line-height:19px}
.foot-line{display:flex;gap:10px;margin-bottom:10px}
.social{display:flex;gap:10px;align-items:center;margin-bottom:16px}
.social i{width:22px;height:22px;border-radius:50%;background:var(--blue);display:block}
.legal{top:3995px;font-size:11px;color:#bbb}
</style>
</head>
<body>

<header class="site-header">
  <div class="abs brand">
    <div class="brand-mark">KRT</div>
    <div class="brand-name">Keystone Health Partners LLC</div>
  </div>
  <div class="abs call">
    <svg width="34" height="34" viewBox="0 0 24 24"><path fill="#173f8e" d="M6.6 10.8a15 15 0 006.6 6.6l2.2-2.2c.3-.3.7-.4 1-.2 1.1.4 2.3.6 3.6.6.6 0 1 .4 1 1V20c0 .6-.4 1-1 1A17 17 0 013 4c0-.6.4-1 1-1h3.5c.6 0 1 .4 1 1 0 1.3.2 2.5.6 3.6.1.3 0 .7-.2 1z"/></svg>
    <div><small>CALL US</small><strong>(555) 274-0193</strong></div>
  </div>
  <nav class="abs nav">
    <span class="active">HOME</span><span>ABOUT US ▾</span><span>SERVICES</span><span>GET A QUOTE</span><span>CONTACT US</span>
  </nav>
</header>

<section class="abs hero" role="img" aria-label="Photo of a diverse team of doctors and consultants meeting around a table" style="background:linear-gradient(100deg,#7c8590 0%,#c9ced4 35%,#e9ecef 65%,#f4f5f7 100%)"></section>
<h1 class="abs hero-title">ADVANCING<br><b>HEALTHCARE</b><br>OPERATIONS</h1>
<a class="btn" style="left:795px;top:468px;width:130px;height:37px;background:var(--blue);font-size:14px">Read More</a>
<div class="abs dots"><i></i><i></i><i class="on"></i><i></i><i></i></div>

<section class="abs welcome"></section>
<svg class="abs" style="left:0;top:640px" width="1200" height="110" viewBox="0 0 1200 110" preserveAspectRatio="none">
  <path d="M0 60 Q600 160 1200 10 L1200 110 L0 110Z" fill="#2b8fd3"/>
  <path d="M0 60 Q600 160 1200 10" fill="none" stroke="#fff" stroke-width="5"/>
</svg>
<div class="abs welcome-photo" role="img" aria-label="Photo of a smiling female doctor with a clipboard, colleagues behind her"></div>
<h2 class="abs welcome-kicker">Welcome to</h2>
<h2 class="abs welcome-title">Keystone Health Partners</h2>
<p class="abs welcome-copy">Keystone Health Partners (KRT) is a healthcare consulting firm skilled at helping physician practices advance their strategic vision in an ever-evolving healthcare system. Keystone Health Partners specializes in revenue cycle optimization, practice management improvement and developing new physician practices. Our technical skills allow us to dig deep into your revenue cycle while our strategic approach ensures we're keeping our eyes on the entire financial picture.</p>
<a class="btn" style="left:603px;top:1135px;width:140px;height:47px;background:var(--navy);font-size:15px">Read More</a>

<section class="abs services"></section>
<h2 class="section-title" style="top:1368px;color:var(--blue)">Our Services</h2>
<div class="rule" style="top:1438px"></div>

<div class="card" style="left:30px">
  <svg width="72" height="72" viewBox="0 0 72 72"><circle cx="36" cy="36" r="24" fill="none" stroke="#2b8fd3" stroke-width="9" stroke-dasharray="30 8"/><circle cx="36" cy="36" r="12" fill="#173f8e"/></svg>
  <h3>REVENUE CYCLE<br>MANAGEMENT</h3>
  <p>But I must explain to you how all this mistaken idea of deno uncing pleasure and praising pain was born and I will give you a comp lete account of the system, and expound the actual great explorer of the truth, the master-build</p>
</div>
<div class="card" style="left:318px">
  <svg width="72" height="72" viewBox="0 0 72 72"><rect x="18" y="10" width="34" height="48" rx="4" fill="#2b8fd3"/><path d="M40 34l10 4v8c0 7-5 11-10 13-5-2-10-6-10-13v-8z" fill="#173f8e"/><path d="M35 45l4 4 7-8" stroke="#fff" stroke-width="3" fill="none"/></svg>
  <h3>REGULATORY<br>COMPLIANCE</h3>
  <p>But I must explain to you how all this mistaken idea of deno uncing pleasure and praising pain was born and I will give you a comp lete account of the system, and expound the actual great explorer of the truth, the master-build</p>
</div>
<div class="card" style="left:608px">
  <svg width="72" height="72" viewBox="0 0 72 72"><circle cx="36" cy="20" r="8" fill="#173f8e"/><circle cx="20" cy="40" r="7" fill="#2b8fd3"/><circle cx="52" cy="40" r="7" fill="#2b8fd3"/><path d="M26 62c0-10 20-10 20 0z" fill="#173f8e"/><path d="M10 62c0-9 20-9 20 0zM42 62c0-9 20-9 20 0z" fill="#2b8fd3"/></svg>
  <h3>HUMAN RESOURCES<br>TRAINING</h3>
  <p>But I must explain to you how all this mistaken idea of deno uncing pleasure and praising pain was born and I will give you a comp lete account of the system, and expound the actual great explorer of the truth, the master-build</p>
</div>
<div class="card" style="left:897px">
  <svg width="72" height="72" viewBox="0 0 72 72"><circle cx="36" cy="24" r="12" fill="none" stroke="#2b8fd3" stroke-width="6"/><circle cx="36" cy="24" r="4" fill="#173f8e"/><path d="M12 40v14l24 8 24-8V40l-24 10z" fill="#173f8e"/></svg>
  <h3>PRACTICE<br>MANAGEMENT</h3>
  <p>But I must explain to you how all this mistaken idea of deno uncing pleasure and praising pain was born and I will give you a comp lete account of the system, and expound the actual great explorer of the truth, the master-build</p>
</div>
<a class="btn" style="left:500px;top:1938px;width:200px;height:54px;background:var(--navy);font-size:22px">Get a Quote</a>

<h2 class="abs contact-title">Contact Us</h2>
<div class="abs contact-item" style="top:2250px">
  <svg width="22" height="22" viewBox="0 0 22 22"><circle cx="11" cy="11" r="11" fill="#2b8fd3"/><path d="M11 5a4 4 0 00-4 4c0 3 4 8 4 8s4-5 4-8a4 4 0 00-4-4z" fill="#fff"/></svg>
  <span>180 Harbor Lane Suite 310 New York,<br>NY 10012</span>
</div>
<div class="abs contact-item" style="top:2315px">
  <svg width="22" height="22" viewBox="0 0 22 22"><circle cx="11" cy="11" r="11" fill="#2b8fd3"/><path d="M8 6l2 3-1 1a7 7 0 003 3l1-1 3 2-1 2c-4 0-9-5-9-9z" fill="#fff"/></svg>
  <span>(555) 274-0193</span>
</div>
<div class="abs contact-item" style="top:2360px">
  <svg width="22" height="22" viewBox="0 0 22 22"><circle cx="11" cy="11" r="11" fill="#2b8fd3"/><rect x="6" y="7" width="10" height="8" fill="#fff"/><path d="M6 7l5 4 5-4" stroke="#2b8fd3" fill="none"/></svg>
  <span>info@krt-health.com</span>
</div>
<div class="field" style="left:90px;top:2430px;width:190px;height:38px">Name</div>
<div class="field" style="left:288px;top:2430px;width:190px;height:38px">E-mail</div>
<div class="field" style="left:90px;top:2475px;width:190px;height:38px">Phone</div>
<div class="field" style="left:288px;top:2475px;width:190px;height:38px">Subject</div>
<div class="field" style="left:90px;top:2520px;width:388px;height:97px">Message</div>
<a class="btn" style="left:90px;top:2637px;width:110px;height:36px;background:var(--navy);font-size:14px">Submit</a>
<div class="abs contact-photo" role="img" aria-label="Photo of a diverse group of smiling doctors and nurses in scrubs"></div>
<div class="abs caption">
  <h4>Healthcare <span>&amp;</span><br>Medical Consultant.</h4>
  <svg class="abs" style="left:400px;top:30px" width="90" height="74" viewBox="0 0 90 74"><line x1="0" y1="0" x2="0" y2="74" stroke="#ccd" stroke-width="1.5"/><path d="M42 37h22M56 29l8 8-8 8" stroke="#2b8fd3" stroke-width="2.5" fill="none"/></svg>
</div>

<section class="abs newsletter" role="img" aria-label="Background photo of medical staff overlaid in deep blue"></section>
<h2 class="section-title" style="top:2910px;color:#fff">Newsletter</h2>
<div class="rule" style="top:2975px;left:580px;width:40px;background:#fff"></div>

<div class="news-card" style="left:178px">
  <div class="ph" role="img" aria-label="Photo of a doctor examining a young patient"></div>
  <div class="body"><h4>Lorem Ipsum is simply dummy text of the printing</h4><p>Sed ut perspiciatis unde omnis iste natus error sit voluptatem accusantiu</p><span class="more">Read More</span></div>
</div>
<div class="news-card" style="left:483px">
  <div class="ph" role="img" aria-label="Photo of two clinicians reviewing a chart"></div>
  <div class="body"><h4>Lorem Ipsum is simply dummy text of the printing</h4><p>Sed ut perspiciatis unde omnis iste natus error sit voluptatem accusantiu</p><span class="more">Read More</span></div>
</div>
<div class="news-card" style="left:787px">
  <div class="ph" role="img" aria-label="Photo of a male and a female doctor standing together"></div>
  <div class="body"><h4>Lorem Ipsum is simply dummy text of the printing</h4><p>Sed ut perspiciatis unde omnis iste natus error sit voluptatem accusantiu</p><span class="more">Read More</span></div>
</div>
<div class="arrow" style="left:98px"><svg width="12" height="12" viewBox="0 0 12 12"><path d="M8 1L3 6l5 5" stroke="#fff" stroke-width="2" fill="none"/></svg></div>
<div class="arrow" style="left:1068px"><svg width="12" height="12" viewBox="0 0 12 12"><path d="M4 1l5 5-5 5" stroke="#fff" stroke-width="2" fill="none"/></svg></div>
<a class="btn" style="left:500px;top:3513px;width:200px;height:50px;background:var(--blue-light);font-size:20px">SUBSCRIBE</a>

<footer class="abs site-footer"></footer>
<div class="abs footer-brand">
  <div class="brand-mark">KRT</div>
  <div class="brand-name">Keystone Health Partners LLC</div>
</div>
<div class="foot-col" style="left:475px">
  <h4>CONTACT US</h4>
  <div class="foot-line"><span>📍</span><span>180 Harbor Lane Suite 310<br>New York, NY 10012</span></div>
  <div class="foot-line"><span>✆</span><span>(555) 274-0193</span></div>
  <div class="foot-line"><span>✉</span><span>info@krt-health.com</span></div>
</div>
<div class="foot-col" style="left:775px">
  <h4>MENU</h4>
  Home<br>About Us<br>Services<br>Get a quote<br>Contact Us
</div>
<div class="foot-col" style="left:948px">
  <h4>CONNECT WITH US</h4>
  <div class="social"><i></i>Community</div>
  <div class="social"><i></i>Updates</div>
  <div class="social"><i></i>Network</div>
</div>
<div class="abs legal" style="left:145px">Terms of service &nbsp;|&nbsp; privacy statement &nbsp;|&nbsp; user agreement &nbsp;|&nbsp; faq &nbsp;|&nbsp; help</div>
<div class="abs legal" style="left:888px">Copyrights @ 2018 All Rights Reserved</div>

</body>
</html>
```